Law firm business cards and stationary
Traditional professional presentation
Law firm business cards and stationary - Law
Creative Brief
Use same font as used in my logo
Other traditional looking fonts will be considered
Professional
Marla J. Pettigrew
Attorney at Law
742 E. 9th Ave, Ste 114 Spokane, WA 99208
(509) TRY-CASE
barrister@mailwove.com
roadcasedefenders.org
Please see uploaded logo. The phone number (509) TRY-CASE is displayed prominently in all marketing. Thank you.

```html
<!DOCTYPE html>
<html lang="en">
<head>
<meta charset="utf-8">
<title>The Pettigrew Firm – Business Card</title>
<link rel="stylesheet" href="https://fonts.googleapis.com/css2?family=Cormorant+Garamond:wght@500;600;700&display=swap">
<style>
  :root {
    --backdrop: #e9ecea;
    --card-white: #ffffff;
    --green: #3fb23a;
    --green-light: #7fd35a;
    --green-deep: #1f8f2a;
    --charcoal: #3b3d3c;
    --ink: #2c2e2d;
    --shadow: rgba(0, 0, 0, 0.18);
  }
  * { margin: 0; padding: 0; box-sizing: border-box; }
  html, body {
    width: 1200px;
    height: 1009px;
    overflow: hidden;
    background: var(--backdrop);
    font-family: "Cormorant Garamond", Georgia, serif;
  }
  .sheet {
    width: 1200px;
    height: 1009px;
    display: flex;
    flex-direction: column;
    align-items: center;
    justify-content: center;
    gap: 44px;
  }
  .card {
    position: relative;
    width: 760px;
    height: 434px;
    border-radius: 14px;
    overflow: hidden;
    box-shadow: 0 10px 28px var(--shadow);
  }

  /* Front */
  .card-front { background: var(--card-white); }
  .card-front .swoosh {
    position: absolute;
    inset: 0;
    width: 100%;
    height: 100%;
  }
  .firm-mark {
    position: absolute;
    left: 56px;
    top: 78px;
    display: flex;
    align-items: center;
    gap: 14px;
  }
  .firm-mark .dot {
    width: 26px;
    height: 26px;
    border-radius: 50%;
    background: var(--green);
  }
  .firm-mark .firm-name {
    font-size: 40px;
    font-weight: 700;
    color: var(--green-deep);
    line-height: 1;
    letter-spacing: 0.5px;
  }
  .contact {
    position: absolute;
    left: 430px;
    top: 60px;
    list-style: none;
    color: var(--ink);
    font-size: 19px;
    font-weight: 600;
    line-height: 1.28;
  }
  .contact li { display: flex; align-items: center; gap: 9px; }
  .contact .address { display: block; margin-bottom: 4px; }
  .contact .icon {
    width: 15px;
    height: 15px;
    border-radius: 3px;
    background: var(--green);
    flex: none;
    display: flex;
    align-items: center;
    justify-content: center;
  }
  .contact .icon svg { width: 11px; height: 11px; }
  .identity {
    position: absolute;
    right: 44px;
    bottom: 34px;
    text-align: right;
    color: var(--card-white);
    font-variant: small-caps;
    font-weight: 600;
  }
  .identity .person { font-size: 34px; letter-spacing: 1px; line-height: 1.1; }
  .identity .title { font-size: 26px; letter-spacing: 1px; line-height: 1.1; }

  /* Back */
  .card-back {
    background: linear-gradient(180deg, var(--green-light) 0%, var(--green) 55%, var(--green-deep) 100%);
    display: flex;
    align-items: center;
    justify-content: center;
    gap: 20px;
  }
  .card-back .dot {
    width: 40px;
    height: 40px;
    border-radius: 50%;
    background: var(--card-white);
  }
  .card-back .firm-name {
    font-size: 64px;
    font-weight: 700;
    color: var(--card-white);
    letter-spacing: 1px;
  }
</style>
</head>
<body>
<main class="sheet">

  <section class="card card-front" aria-label="Business card front">
    <svg class="swoosh" viewBox="0 0 760 434" preserveAspectRatio="none" aria-hidden="true">
      <defs>
        <linearGradient id="greenBand" x1="0" y1="0" x2="0" y2="1">
          <stop offset="0" stop-color="#7fd35a"/>
          <stop offset="0.5" stop-color="#3fb23a"/>
          <stop offset="1" stop-color="#1f8f2a"/>
        </linearGradient>
      </defs>
      <path d="M0,200 C220,292 520,318 760,286 L760,300 C520,330 220,310 0,232 Z" fill="#3b3d3c"/>
      <path d="M0,262 C210,338 500,352 760,318 L760,434 L0,434 Z" fill="url(#greenBand)"/>
    </svg>

    <div class="firm-mark">
      <span class="dot"></span>
      <span class="firm-name">The Pettigrew Firm</span>
    </div>

    <ul class="contact">
      <li class="address">742 E. 9th Ave, Ste 114<br>Spokane, WA 99208</li>
      <li>
        <span class="icon"><svg viewBox="0 0 12 12"><path d="M3 1 L5 3.5 L4 4.6 Q5 7 7.4 8 L8.5 7 L11 9 L10 11 Q3 11 1 3 Z" fill="#fff"/></svg></span>
        (509) TRY-CASE
      </li>
      <li>
        <span class="icon"><svg viewBox="0 0 12 12"><rect x="1" y="3" width="10" height="7" fill="none" stroke="#fff" stroke-width="1.3"/><path d="M1 3 L6 7 L11 3" fill="none" stroke="#fff" stroke-width="1.3"/></svg></span>
        barrister@mailwove.com
      </li>
      <li>
        <span class="icon"><svg viewBox="0 0 12 12"><circle cx="6" cy="6" r="4.5" fill="none" stroke="#fff" stroke-width="1.2"/><path d="M1.5 6 H10.5 M6 1.5 Q3.5 6 6 10.5 Q8.5 6 6 1.5" fill="none" stroke="#fff" stroke-width="1"/></svg></span>
        roadcasedefenders.org
      </li>
    </ul>

    <div class="identity">
      <p class="person">Marla J. Pettigrew</p>
      <p class="title">Attorney at Law</p>
    </div>
  </section>

  <section class="card card-back" aria-label="Business card back">
    <span class="dot"></span>
    <span class="firm-name">The Pettigrew Firm</span>
  </section>

</main>
</body>
</html>
```